Business Card Design for Real Estate Company

I am looking for a business card design that will catch my client's attention.

Industry/Entity Type

Business

Requirements
Must have
• Please have the following information in the business card design. You can substitute the "Office, Mobile, email, and web" with an icon or some other design you may think will go well with the business card.

Derek Osmund
482 W. Fenwick St., Suite 310
Pasadena, CA 91348
Office: 626.748.1196
Mobile: 626.913.4071
email: Derek@CrestviewPropertyWalk.example
web: www.CrestviewPropertyWalk.example

```html
<!DOCTYPE html>
<html lang="en">
<head>
<meta charset="utf-8">
<title>Crestview Property Walk — Business Card</title>
<link rel="stylesheet" href="https://fonts.googleapis.com/css2?family=Lato:wght@700&family=Tenor+Sans&display=swap">
<style>
  :root {
    --backdrop: #ededed;
    --card: #fbfbfb;
    --brown: #5a4629;
    --text: #55524c;
    --orange: #e0782b;
    --blue: #2f6fa8;
    --sky: #7fb0d8;
    --olive: #8a9a3a;
    --yellow: #d9c81e;
    --shadow: rgba(0, 0, 0, 0.12);
  }
  * { box-sizing: border-box; margin: 0; padding: 0; }
  html, body {
    width: 1200px;
    height: 795px;
    overflow: hidden;
    background: var(--backdrop);
  }
  .canvas {
    position: relative;
    width: 1200px;
    height: 795px;
  }
  .card {
    position: absolute;
    top: 249px;
    width: 520px;
    height: 297px;
    background: var(--card);
    box-shadow: 0 10px 26px var(--shadow);
    font-family: "Tenor Sans", sans-serif;
    color: var(--text);
    overflow: hidden;
  }
  .card--front { left: 50px; }
  .card--back { left: 630px; }

  /* wordmark */
  .wordmark {
    display: flex;
    align-items: center;
    gap: 8px;
    color: var(--brown);
    font-family: "Tenor Sans", sans-serif;
    white-space: nowrap;
  }
  .wordmark__dot {
    width: 12px;
    height: 12px;
    border-radius: 50%;
    background: var(--olive);
    flex: none;
  }

  /* front */
  .front__illustration {
    position: absolute;
    left: 0;
    top: 58px;
    width: 218px;
    height: 239px;
    border-radius: 0 120px 0 0;
    background:
      radial-gradient(circle at 22% 30%, rgba(47, 111, 168, 0.55), transparent 32%),
      radial-gradient(circle at 48% 22%, rgba(217, 200, 30, 0.6), transparent 34%),
      radial-gradient(circle at 78% 38%, rgba(224, 120, 43, 0.55), transparent 32%),
      radial-gradient(circle at 62% 12%, rgba(127, 176, 216, 0.6), transparent 30%),
      radial-gradient(circle at 30% 62%, rgba(138, 154, 58, 0.5), transparent 38%),
      linear-gradient(180deg, #eef0e4 0%, #e9e6dc 100%);
  }
  .card--front .wordmark {
    position: absolute;
    right: 30px;
    top: 110px;
    font-size: 20px;
  }
  .front__web {
    position: absolute;
    right: 30px;
    top: 146px;
    font-size: 11px;
    color: var(--brown);
    letter-spacing: 0.3px;
  }

  /* back */
  .card--back .wordmark {
    position: absolute;
    right: 40px;
    top: 40px;
    font-size: 22px;
  }
  .contact {
    position: absolute;
    left: 34px;
    right: 40px;
    bottom: 36px;
  }
  .contact__name {
    font-family: "Lato", sans-serif;
    font-weight: 700;
    font-size: 19px;
    color: var(--brown);
    margin-bottom: 8px;
  }
  .contact__rule {
    height: 1px;
    background: var(--orange);
    margin: 6px 0;
  }
  .contact__line {
    font-size: 12.5px;
    line-height: 19px;
    color: var(--text);
  }
  .contact__label { color: var(--orange); margin-right: 4px; }
  .contact__label--mobile { color: var(--olive); }
  .contact__label--email { color: var(--blue); }
  .contact__sep { color: var(--orange); margin: 0 6px; }
</style>
</head>
<body>
<main class="canvas">

  <section class="card card--front" aria-label="Card front">
    <div class="front__illustration" role="img" aria-label="Large illustrated tree with dark branches and leaves in blue, olive, yellow and orange"></div>
    <div class="wordmark">
      <span class="wordmark__dot"></span>
      <span class="wordmark__name">Crestview Property Walk</span>
    </div>
    <p class="front__web">www.CrestviewPropertyWalk.example</p>
  </section>

  <section class="card card--back" aria-label="Card back">
    <div class="wordmark">
      <span class="wordmark__dot"></span>
      <span class="wordmark__name">Crestview Property Walk</span>
    </div>

    <div class="contact">
      <h1 class="contact__name">Derek Osmund</h1>
      <div class="contact__rule"></div>
      <p class="contact__line">
        <span class="contact__label">T</span>626.748.1196<span class="contact__sep">|</span><span class="contact__label contact__label--mobile">M</span>626.913.4071
      </p>
      <p class="contact__line">
        <span class="contact__label contact__label--email">E</span>Derek@CrestviewPropertyWalk.example
      </p>
      <div class="contact__rule"></div>
      <p class="contact__line">482 W. Fenwick St., Suite 310, Pasadena, CA 91348</p>
    </div>
  </section>

</main>
</body>
</html>
```